Brell Harbor Company Business Cards

Front and Back Business Card - logo and text setup - cool design. I need workable photoshop or illustrator files so I can setup each employee card with design that is created
Updates

Hi everyone, thank you for the great entries. Please no more white and blue cards - there are so many already - black and silver only now please. thanks!

Target Market(s)

Construction Industry - Facility Managers

Industry/Entity Type

Construction

Contact Information for Business Card

I really like contemporary simplistic looks - clean neat....not opposed to seeing some black backrounds

Requirements
Must have
• Logo/website address with design on front only - www.brellharbor-example.com (logo attached)
• Back:
• Name/Title/Company Address/Phone/email address
Nice to have
• Cool design
Should not have
• Nothing gimmicky like Fire or Water - since we are a Fire Protection company - it has all been done

```html
<!DOCTYPE html>
<html lang="en">
<head>
<meta charset="utf-8">
<title>Brell Harbor Company Business Cards</title>
<link href="https://fonts.googleapis.com/css2?family=Open+Sans:wght@400;600;700&display=swap" rel="stylesheet">
<style>
  :root {
    --backdrop: #4a4441;
    --card: #1f2125;
    --silver: #b9bcc0;
    --ink: #f2f2f2;
    --navy: #2f4a8a;
    --coral: #e8483a;
    --rule: #d9d9d9;
  }
  * { margin: 0; padding: 0; box-sizing: border-box; }
  html, body {
    width: 1200px; height: 864px; overflow: hidden;
    background: var(--backdrop);
    font-family: "Open Sans", Arial, sans-serif;
  }
  .canvas { position: relative; width: 1200px; height: 864px; }
  .card {
    position: absolute; left: 290px;
    width: 620px; height: 354px;
    background: var(--card);
    border-radius: 3px;
    box-shadow: 0 10px 28px rgba(0,0,0,.35);
    overflow: hidden;
  }
  .card--front { top: 52px; }
  .card--back { top: 458px; }

  /* front */
  .front-name {
    position: absolute; left: 0; right: 0; top: 118px;
    text-align: center;
    font-weight: 700; font-size: 50px; letter-spacing: -1px;
    color: var(--silver);
  }
  .front-url {
    position: absolute; left: 0; right: 0; top: 232px;
    text-align: center;
    font-size: 15px; letter-spacing: 7px;
    color: var(--ink);
  }

  /* back */
  .back-name {
    position: absolute; right: 40px; top: 50px;
    font-weight: 700; font-size: 40px; letter-spacing: -1px;
    color: var(--navy);
  }
  .person { position: absolute; left: 40px; top: 46px; }
  .person__name { font-size: 22px; font-weight: 600; color: var(--navy); letter-spacing: .5px; line-height: 1.1; }
  .person__title { font-size: 15px; color: var(--coral); letter-spacing: .5px; }
  .contact { position: absolute; left: 40px; top: 112px; list-style: none; }
  .contact li {
    display: flex; align-items: center; gap: 10px;
    font-size: 15px; color: var(--ink); line-height: 24px;
  }
  .contact svg { width: 13px; height: 13px; fill: var(--navy); flex: none; }
  .divider {
    position: absolute; left: 40px; right: 40px; top: 196px;
    height: 1px; background: var(--rule);
  }
  .address {
    position: absolute; right: 40px; top: 222px;
    text-align: right; font-size: 17px; line-height: 26px;
    color: var(--ink);
  }
</style>
</head>
<body>
<main class="canvas">
  <section class="card card--front" aria-label="Card front">
    <div class="front-name">Brell Harbor</div>
    <div class="front-url">www.brellharbor-example.com</div>
  </section>

  <section class="card card--back" aria-label="Card back">
    <div class="back-name">Brell Harbor</div>
    <div class="person">
      <div class="person__name">MARA QUILL</div>
      <div class="person__title">PRESIDENT</div>
    </div>
    <ul class="contact">
      <li>
        <svg viewBox="0 0 16 16" aria-hidden="true"><path d="M2 4c0-1.5 2-3 6-3s6 1.5 6 3v2h-3V4.5H5V6H2z M3 8h10l1 6H2z"/></svg>
        (555) 014-2870
      </li>
      <li>
        <svg viewBox="0 0 16 16" aria-hidden="true"><path d="M4 1h8v4H4z M1 6h14v6h-3v3H4v-3H1z M5 10v4h6v-4z"/></svg>
        (555) 014-2871
      </li>
      <li>
        <svg viewBox="0 0 16 16" aria-hidden="true"><path d="M1 3h14v10H1z M2 4.2v.6l6 4 6-4v-.6z" fill-rule="evenodd"/></svg>
        info@brellharbor-example.com
      </li>
    </ul>
    <div class="divider"></div>
    <address class="address" style="font-style:normal">
      48 Quarry Lane<br>
      Westmere, NY 10990<br>
      www.brellharbor-example.com
    </address>
  </section>
</main>
</body>
</html>
```